Need a image for a Chirpwall ad campaign

Need a image designed for a Chirpwall ad campaign. We are setting up a Chirpwall campaign advertising on Chirpwall for people who would want to get into modelling. We accept people aged 4+ . We want them to go to glowrunwayhub dot com to sign up and apply. We need this image to comply with Chirpwall ad policies. It can't have more than 20% text on it.

Maybe just say Become a Model or something
Glow Runway Hub or something your choice.

What size should my ad image be?

The best image size to use for your ad depends on what type of ad you're creating, but a best practice is to size your images to be 1200 x 628 pixels. The Promo Spec Handbook contains all of the specifications around the recommended ad image sizes for each ad type. If your image is larger or smaller than the dimensions specified in the Promo Spec Handbook, it will be automatically resized to fit in the ad. Animated or flash images aren't supported.

Keep in mind that your ad may not contain more than 20% text in the ad's image.

People who would want to get into modelling

Advertising

Sans Serif

Designer to choose colors to be used in the design.

Must have
• Must tie in with the main website glowrunwayhub dot com

```html
<!DOCTYPE html>
<html lang="en">
<head>
<meta charset="utf-8">
<title>Become a Model – Glow Runway Hub</title>
<link href="https://fonts.googleapis.com/css2?family=Playfair+Display:wght@400&family=Lato:wght@700&display=swap" rel="stylesheet">
<style>
  :root {
    --tan: #b39d7d;
    --sand: #c8b597;
    --skin: #b88f7c;
    --cocoa: #5a3837;
    --cream: #ffffff;
  }
  html, body {
    margin: 0;
    padding: 0;
    overflow: hidden;
    width: 1200px;
    height: 628px;
  }
  .ad {
    position: relative;
    width: 1200px;
    height: 628px;
    overflow: hidden;
    background: var(--tan);
  }
  .ad__portrait {
    position: absolute;
    inset: 0;
    background:
      radial-gradient(ellipse 260px 230px at 560px 330px, var(--skin) 0%, rgba(184,143,124,0.6) 50%, rgba(184,143,124,0) 100%),
      radial-gradient(ellipse 380px 420px at 600px 300px, rgba(94,69,53,0.9) 0%, rgba(94,69,53,0.55) 55%, rgba(94,69,53,0) 100%),
      radial-gradient(ellipse 260px 140px at 140px 460px, rgba(224,214,200,0.85) 0%, rgba(224,214,200,0) 100%),
      linear-gradient(90deg, var(--sand) 0%, var(--tan) 40%, #8f7a60 100%);
  }
  .ad__flourish {
    position: absolute;
    left: 430px;
    width: 340px;
    height: 54px;
    background: linear-gradient(90deg, rgba(255,255,255,0) 0%, rgba(255,255,255,0.22) 50%, rgba(255,255,255,0) 100%);
  }
  .ad__flourish--top { top: 126px; }
  .ad__flourish--bottom { top: 444px; }
  .ad__message {
    position: absolute;
    left: 0;
    top: 0;
    width: 1200px;
    height: 628px;
  }
  .headline {
    font-family: "Playfair Display", serif;
    font-weight: 400;
    fill: var(--cream);
  }
  .site-link {
    font-family: "Lato", sans-serif;
    font-weight: 700;
    font-size: 16px;
    fill: var(--cream);
  }
</style>
</head>
<body>
<main class="ad">
  <div class="ad__portrait" role="img" aria-label="Soft-focus portrait photograph of a young woman with long brown hair"></div>
  <div class="ad__flourish ad__flourish--top" role="img" aria-label="Decorative scroll ornament"></div>
  <div class="ad__flourish ad__flourish--bottom" role="img" aria-label="Decorative scroll ornament"></div>

  <svg class="ad__message" viewBox="0 0 1200 628" aria-label="Become a Model – www.glowrunwayhub.com">
    <text class="headline" x="600" y="276" font-size="100" text-anchor="middle" textLength="510" lengthAdjust="spacingAndGlyphs">BECOME A</text>
    <text class="headline" x="600" y="386" font-size="118" text-anchor="middle" textLength="510" lengthAdjust="spacingAndGlyphs">MODEL</text>
    <text class="site-link" x="600" y="422" text-anchor="middle" textLength="490" lengthAdjust="spacing">WWW.GLOWRUNWAYHUB.COM</text>
  </svg>
</main>
</body>
</html>
```